Blue Heron Courier & Delivery Services needs a flyer

We need an introductory flyer for a new company based in Yellowknife, Northwest Territories,Canada. Our company name is Blue Heron Courier & Delivery Services. We will be handling envelopes and small packages up to 20 pounds. We expect 20 percent of our business to come from residential customers and 80 percent from the business community including lawyers, doctors, engineers and government offices. The main message that we will try to convey in this flyer is that we are a new and exciting company that promises to make 100% customer satisfaction our number one goal. I would like the layout to be elegant and simple and certainly not cluttered. It will be a single sided flyer. Text should be easy to read and most likely at most two fonts. I would like one stunning image or photo relating to the courier business and message. There should be plenty of white space throughout the flyer and nice margins on all sides. I would like my flyer to be 8.5 inches by 11 inches and it should read from top to bottom. . I would like a nice big bold headline that in some way mentions " Special Offer- Up to 100% Off. You can change the wording if you have a better idea. Throughout the flyer you can highlight and italicize for emphasis. Please try to use bullet points for my five main reasons for hiring our company which are: you will be 100% satisfied with each delivery or you will be given a complete refund no questions asked, your envelope or package will be delivered on time every time, you will always be treated throughout the delivery process in a professional manner, you will be given the widest selection in Yellowknife of price points and delivery options , you can trust us with your most important and time sensitive deliveries. Try to incorporate something next to these five points to really draw attention like a check mark, star etc.... I would prefer if my company name and contact info is in the bottom third of the flyer. My email is blueheroncourieryk@mailbox-example.net. My phone number is 867-312-7794. It might be a good idea to have my phone number also at the top of the flyer someplace after the headline saying like Call Now!!! you can use boxes, borders and contrasting bold colors to bring flyer to life. I have a testimonial from a business owner that I dealt with when I ran another business which would be nice to have included . " While receiving daily deliveries for 18 years from Calvin Marsh I found him to be punctual , reliable and efficient " Glen Potter, owner of Potter and Lindqvist Trading LTD, Yellowknife,NWT. I thought perhaps at the top of flyer after the headline perhaps in some way you could say Yellowknife's newest and best courier and delivery service is pleased to offer the following stunning discounts: then you could list the three special offers: 1) First 5 businesses to book regular scheduled deliveries will get 100% off their first delivery. 2) First 5 businesses to book a single delivery will get 50% off that delivery. 3) First 5 residential customers to book a delivery will receive 25% off that delivery. I thought you could mention my name somewhere. Calvin Marsh. Owner has lived in Yellowknife for 42 years and has 20 years experience doing performing important and time sensitive deliveries. Perhaps you could mention somewhere that we will have a couple of ongoing discounts also which will be 1) seniors discounts. 2) regular scheduled deliveries discounts. I have suggested colors but if you have other ideas I would certainly look at them. Our business tag line is. On Time Every Time
Target Market(s)
Business owners typically males 30-50 years old
Industry/Entity Type
Delivery Service
Requirements
Must have
- Done in CMYK mode sufficient bleed size for printing
Nice to have
- Nothing set in stone. I recently had my logo design uploaded to this brief. It is up to you if you feel it should be included in the flyer.
Should not have
- I am willing to look at any design

```html
<!DOCTYPE html>
<html lang="en">
<head>
<meta charset="utf-8">
<title>Blue Heron Courier &amp; Delivery Services – Flyer</title>
<link rel="stylesheet" href="https://fonts.googleapis.com/css2?family=Arimo:ital,wght@0,400;0,700;1,400&family=Exo+2:wght@400&display=swap">
<style>
  :root {
    --stage: #2b2b2b;
    --black: #050505;
    --panel: #1c1c1c;
    --panel-dark: #111111;
    --yellow: #ffcc00;
    --gold: #c9a227;
    --blue: #1a9be0;
    --white: #f2f2f2;
    --ink: #111111;
  }
  * { box-sizing: border-box; margin: 0; padding: 0; }
  html, body { width: 1200px; height: 1000px; overflow: hidden; }
  body {
    background: var(--stage);
    font-family: "Arimo", Arial, sans-serif;
    position: relative;
  }
  .flyer {
    position: absolute;
    left: 293px; top: 130px;
    width: 596px; height: 773px;
    background: var(--black);
    overflow: hidden;
    box-shadow: 0 8px 24px rgba(0,0,0,.5);
  }
  .hero-photo {
    position: absolute; left: 0; top: 0; width: 596px; height: 230px;
    background: linear-gradient(90deg, #d8d8d8 0%, #9aa4ad 25%, #c9b98f 45%, #e9e4d6 55%, #b79f74 75%, #d6d6d6 100%);
  }
  .brand-box {
    position: absolute; right: 0; top: 10px; width: 199px; height: 75px;
    background: var(--yellow);
    display: flex; align-items: center; justify-content: center; text-align: center;
    color: var(--ink); font-weight: 700; font-size: 15px; line-height: 19px;
  }
  .call-now {
    position: absolute; left: 0; top: 194px; width: 596px; height: 36px;
  }
  .call-now svg { position: absolute; left: 157px; top: 0; }
  .call-now span {
    position: absolute; left: 157px; top: 0; width: 280px; height: 36px;
    display: flex; align-items: center; justify-content: center;
    font-weight: 700; font-size: 17px; color: var(--ink);
  }
  .offer { position: absolute; left: 0; top: 230px; width: 596px; text-align: center; }
  .offer-headline {
    margin-top: 22px;
    font-family: "Exo 2", Arial, sans-serif;
    font-size: 37px; color: var(--yellow); font-weight: 400; letter-spacing: .5px;
  }
  .offer-intro { margin-top: 10px; font-size: 17.5px; line-height: 20px; color: var(--blue); }
  .offer-list { margin-top: 12px; list-style: none; font-size: 11.2px; line-height: 20px; color: var(--white); letter-spacing: .2px; }
  .divider { position: absolute; left: 0; }
  .reasons {
    position: absolute; left: 0; top: 450px; width: 387px; height: 278px;
    background: linear-gradient(180deg, var(--panel) 0%, var(--panel-dark) 100%);
  }
  .reasons-title { text-align: center; color: var(--blue); font-size: 22px; margin-top: 6px; letter-spacing: .5px; }
  .reason-list { list-style: none; }
  .reason { position: absolute; left: 0; width: 387px; }
  .reason-marker { position: absolute; left: 0; top: 0; }
  .reason-text { position: absolute; left: 75px; top: -6px; width: 290px; color: var(--yellow); font-size: 12.6px; line-height: 15px; text-align: justify; }
  .testimonial-panel {
    position: absolute; left: 390px; top: 450px; width: 206px; height: 278px;
    background: linear-gradient(180deg, #262626 0%, #141414 100%);
  }
  .quote { position: absolute; left: 18px; top: 20px; width: 152px; color: var(--blue); font-style: italic; font-size: 12px; line-height: 14px; letter-spacing: .8px; text-align: justify; }
  .quote cite { display: block; font-size: 8.6px; line-height: 11px; letter-spacing: .9px; }
  .owner-badge { position: absolute; left: 46px; top: 142px; }
  .owner-badge span {
    position: absolute; left: 0; top: 0; width: 92px; height: 44px;
    display: flex; align-items: center; justify-content: center; text-align: center;
    font-weight: 700; font-size: 13px; line-height: 15px; color: var(--ink);
  }
  .owner-bio { position: absolute; left: 18px; top: 192px; width: 152px; color: var(--yellow); font-size: 11.8px; line-height: 13px; letter-spacing: .3px; text-align: justify; }
  .owner-bio .spaced { letter-spacing: 3px; }
  .contact-bar {
    position: absolute; left: 0; top: 728px; width: 596px; height: 45px;
    background: var(--black); color: var(--blue); font-size: 12px;
    display: flex; align-items: center; justify-content: center; letter-spacing: .3px;
  }
</style>
</head>
<body>
<main class="flyer">
  <div class="hero-photo" role="img" aria-label="Photo of a courier in a blue cap carrying a cardboard box through a warehouse aisle"></div>
  <div class="brand-box">Blue Heron<br>Courier &amp; Delivery<br>Services</div>
  <div class="call-now">
    <svg width="280" height="36" viewBox="0 0 280 36" aria-hidden="true"><path d="M6 0 H274 L280 36 H0 Z" fill="var(--yellow)"/></svg>
    <span>Call Now!!! 867-312-7794</span>
  </div>
  <svg class="divider" style="top:228px" width="596" height="12" viewBox="0 0 596 12" aria-hidden="true"><path d="M0 10 Q298 -2 596 10" stroke="var(--gold)" stroke-width="3" fill="none"/></svg>

  <section class="offer">
    <h1 class="offer-headline">Special Offer Up to 100% Off</h1>
    <p class="offer-intro">Yellowknife's newest and best courier and delivery service<br>is pleased to offer the following stunning discounts</p>
    <ul class="offer-list">
      <li>First 5 businesses to book regular scheduled deliveries will get 100% off their first delivery.</li>
      <li>First 5 businesses to book a single delivery will get 50% off that delivery.</li>
      <li>First 5 residential customers to book a delivery will receive 25% off that delivery</li>
    </ul>
  </section>

  <svg class="divider" style="top:430px" width="596" height="22" viewBox="0 0 596 22" aria-hidden="true"><path d="M0 20 Q298 0 596 20" stroke="var(--gold)" stroke-width="3" fill="none"/></svg>

  <section class="reasons">
    <h2 class="reasons-title">WHY US?</h2>
    <ul class="reason-list">
      <li class="reason" style="top:46px">
        <svg class="reason-marker" width="62" height="34" viewBox="0 0 62 34" aria-hidden="true"><rect width="50" height="34" fill="var(--yellow)"/><path d="M50 0 H56 V34 H50 Z" fill="#b38f00"/><polygon points="47,4 50.6,13 60,13 52.4,18.6 55.2,28 47,22.4 38.8,28 41.6,18.6 34,13 43.4,13" fill="var(--yellow)" stroke="var(--ink)" stroke-width="1.3"/></svg>
        <p class="reason-text">you will be 100% satisfied with each delivery or you will be given a complete refund no questions asked.</p>
      </li>
      <li class="reason" style="top:101px">
        <svg class="reason-marker" width="62" height="34" viewBox="0 0 62 34" aria-hidden="true"><rect width="50" height="34" fill="var(--yellow)"/><path d="M50 0 H56 V34 H50 Z" fill="#b38f00"/><polygon points="47,4 50.6,13 60,13 52.4,18.6 55.2,28 47,22.4 38.8,28 41.6,18.6 34,13 43.4,13" fill="var(--yellow)" stroke="var(--ink)" stroke-width="1.3"/></svg>
        <p class="reason-text">your envelope or package will be delivered on time every time.</p>
      </li>
      <li class="reason" style="top:147px">
        <svg class="reason-marker" width="62" height="34" viewBox="0 0 62 34" aria-hidden="true"><rect width="50" height="34" fill="var(--yellow)"/><path d="M50 0 H56 V34 H50 Z" fill="#b38f00"/><polygon points="47,4 50.6,13 60,13 52.4,18.6 55.2,28 47,22.4 38.8,28 41.6,18.6 34,13 43.4,13" fill="var(--yellow)" stroke="var(--ink)" stroke-width="1.3"/></svg>
        <p class="reason-text">you will always be treated throughout the delivery process in a professional manner.</p>
      </li>
      <li class="reason" style="top:193px">
        <svg class="reason-marker" width="62" height="34" viewBox="0 0 62 34" aria-hidden="true"><rect width="50" height="34" fill="var(--yellow)"/><path d="M50 0 H56 V34 H50 Z" fill="#b38f00"/><polygon points="47,4 50.6,13 60,13 52.4,18.6 55.2,28 47,22.4 38.8,28 41.6,18.6 34,13 43.4,13" fill="var(--yellow)" stroke="var(--ink)" stroke-width="1.3"/></svg>
        <p class="reason-text">you will be given the widest selection in Yellowknife of price points and delivery options.</p>
      </li>
      <li class="reason" style="top:238px">
        <svg class="reason-marker" width="62" height="34" viewBox="0 0 62 34" aria-hidden="true"><rect width="50" height="34" fill="var(--yellow)"/><path d="M50 0 H56 V34 H50 Z" fill="#b38f00"/><polygon points="47,4 50.6,13 60,13 52.4,18.6 55.2,28 47,22.4 38.8,28 41.6,18.6 34,13 43.4,13" fill="var(--yellow)" stroke="var(--ink)" stroke-width="1.3"/></svg>
        <p class="reason-text">you can trust us with your most important and time sensitive deliveries.</p>
      </li>
    </ul>
  </section>

  <aside class="testimonial-panel">
    <blockquote class="quote">"While receiving daily deliveries for 18 years from Calvin Marsh I found him to be punctual , reliable and efficient".
      <cite>Glen Potter, owner of Potter and Lindqvist Trading LTD, Yellowknife,NWT.</cite>
    </blockquote>
    <div class="owner-badge">
      <svg width="92" height="44" viewBox="0 0 92 44" aria-hidden="true"><path d="M0 0 H92 L86 8 V38 Q46 46 6 38 V8 Z" fill="var(--yellow)"/><path d="M0 0 H92 L86 8 H6 Z" fill="#e0a800"/></svg>
      <span>Calvin<br>Marsh</span>
    </div>
    <p class="owner-bio"><span class="spaced">Owner has lived in</span> Yellowknife for 42 years and has 20 years experience performing important and time sensitive deliveries.</p>
  </aside>

  <footer class="contact-bar">blueheroncourieryk@mailbox-example.net &nbsp;|&nbsp; 867-312-7794</footer>
</main>
</body>
</html>
```